Quilvo Garage Doors Business Card

I need a Business Card for my garage door business:
Quilvo Garage Doors.
please add:
logo
phone number: 855-3-QUILVO
(853-392)

email: service@quilvogaragedoors.com
website: www.quilvogaragedoors.com

The attached image is recommendation ONLY.

```html
<!DOCTYPE html>
<html lang="en">
<head>
<meta charset="UTF-8">
<title>Quilvo Garage Doors Business Card</title>
<link href="https://fonts.googleapis.com/css2?family=Poppins:wght@400;500;600&display=swap" rel="stylesheet">
<style>
  :root {
    --teal: #4fc3d0;
    --teal-faint: #e9f7f9;
    --ink: #141414;
    --card: #ffffff;
    --bg: #2b2b2d;
  }
  * { margin: 0; padding: 0; box-sizing: border-box; }
  html, body { width: 1200px; height: 900px; overflow: hidden; }
  body {
    background: var(--bg);
    font-family: "Poppins", sans-serif;
    color: var(--ink);
    position: relative;
  }
  .card {
    position: absolute;
    width: 560px;
    height: 320px;
    background: var(--card);
    border-radius: 22px;
    overflow: hidden;
    box-shadow: 0 14px 30px rgba(0,0,0,0.45);
  }
  /* back side */
  .card-back { left: 80px; top: 110px; }
  .back-brand {
    position: absolute;
    left: 0; right: 0; top: 110px;
    display: flex; align-items: center; justify-content: center; gap: 14px;
  }
  .brand-mark {
    width: 34px; height: 34px;
    background: var(--teal);
    border-radius: 8px;
  }
  .back-brand .brand-name {
    font-size: 30px; font-weight: 500; color: var(--ink);
  }
  .back-website {
    position: absolute;
    left: 0; right: 0; top: 236px;
    text-align: center;
    font-size: 14px; font-weight: 600; letter-spacing: 0.3px;
  }
  .back-website .domain { color: var(--teal); }

  /* front side */
  .card-front { left: 560px; top: 470px; }
  .watermark {
    position: absolute;
    left: 270px; top: 70px;
    width: 190px; height: 190px;
    border-radius: 50%;
    background: var(--teal-faint);
  }
  .front-brand {
    position: absolute;
    left: 34px; top: 58px;
    display: flex; align-items: center; gap: 14px;
  }
  .front-brand .brand-mark { width: 60px; height: 60px; border-radius: 12px; }
  .front-brand .brand-name {
    font-size: 25px; font-weight: 500; line-height: 1.1; width: 150px;
  }
  .person {
    position: absolute;
    right: 30px; top: 136px;
    text-align: right;
  }
  .person-name { font-size: 21px; font-weight: 600; letter-spacing: 0.6px; }
  .person-title { font-size: 12px; font-weight: 500; color: var(--teal); letter-spacing: 0.5px; }
  .divider {
    position: absolute;
    left: 0; right: 0; top: 196px;
    height: 2px; background: var(--teal);
  }
  .contacts {
    position: absolute;
    left: 30px; top: 212px;
    list-style: none;
  }
  .contacts li {
    display: flex; align-items: center; gap: 10px;
    font-size: 14px; font-weight: 600; letter-spacing: 0.4px;
    line-height: 28px;
  }
  .contacts svg { width: 12px; height: 12px; flex: none; }
</style>
</head>
<body>

  <section class="card card-back">
    <div class="back-brand">
      <span class="brand-mark"></span>
      <span class="brand-name">Quilvo Garage Doors</span>
    </div>
    <p class="back-website">www.<span class="domain">quilvogaragedoors</span>.com</p>
  </section>

  <section class="card card-front">
    <div class="watermark"></div>
    <div class="front-brand">
      <span class="brand-mark"></span>
      <span class="brand-name">Quilvo Garage Doors</span>
    </div>
    <div class="person">
      <p class="person-name">Marlen Okafor</p>
      <p class="person-title">Director</p>
    </div>
    <div class="divider"></div>
    <ul class="contacts">
      <li>
        <svg viewBox="0 0 12 12"><path d="M2 1l2.5 0 1 3-1.5 1a6 6 0 0 0 3 3l1-1.5 3 1V10a1 1 0 0 1-1 1A9 9 0 0 1 1 2a1 1 0 0 1 1-1z" fill="var(--teal)"/></svg>
        855-3-QUILVO(853-392)
      </li>
      <li>
        <svg viewBox="0 0 12 12"><rect x="1" y="2.5" width="10" height="7" rx="1" fill="none" stroke="var(--teal)" stroke-width="1.2"/><path d="M1.5 3l4.5 3.5L10.5 3" fill="none" stroke="var(--teal)" stroke-width="1.2"/></svg>
        service@quilvogaragedoors.com
      </li>
      <li>
        <svg viewBox="0 0 12 12"><circle cx="6" cy="6" r="5" fill="none" stroke="var(--teal)" stroke-width="1.2"/><path d="M1 6h10M6 1c-2.5 3-2.5 7 0 10M6 1c2.5 3 2.5 7 0 10" fill="none" stroke="var(--teal)" stroke-width="1"/></svg>
        www.quilvogaragedoors.com
      </li>
    </ul>
  </section>

</body>
</html>
```